Flyer für Kinderschminken, Schwangerschaftsbemalung, Glitzertattoos
Zielgruppe
Ich biete Kinderschminken, Glitzer-Tattoos, Wundenschminken und Schwangerschaftsbemalung an so wie Vermietung von einer Popkornmaschine.
Aufgabenstellung
Schön wäre es, wenn Sie sich an meiner Internetseite orientieren.
Wichtig ist das Logo und eine Übersicht meiner Leistung.
Gern würde ich über den Flyer vermitteln, was mich abhebt beziehungsweise vorauf ich acht lege und was eine professionelle Kinderschminktante aus macht.
Ich achte auf Hygiene, bilde mich immer wieder weiter, besuche Fortbildungen und habe hochwertige Produkte / Farben, die eine EU-Kosmetik Verordnung haben und somit hautverträglich sind.
Ich habe an einen A6 Flyer gedacht beidseitig bin aber offen für neue Ideen und Vorschläge.
https://frau-sonnenfeld.de

```html
<!DOCTYPE html>
<html lang="de">
<head>
<meta charset="utf-8">
<title>Frau Sonnenfeld – Flyer</title>
<link rel="stylesheet" href="https://fonts.googleapis.com/css2?family=Roboto:wght@300;400;700&family=Roboto+Condensed:wght@700&display=swap">
<style>
  :root{
    --teal:#1a9fb0;
    --teal-dark:#148999;
    --white:#ffffff;
    --ink:#4a4a4a;
    --soft:#eceeee;
    --stage:#8a867b;
  }
  *{box-sizing:border-box;margin:0;padding:0}
  html,body{width:960px;height:1200px;overflow:hidden}
  body{background:var(--stage);font-family:"Roboto",Arial,sans-serif;position:relative}
  .sheet{position:absolute;top:289px;width:440px;height:622px;background:var(--white);overflow:hidden;box-shadow:0 10px 30px rgba(0,0,0,.25)}
  .sheet--back{left:30px}
  .sheet--front{left:490px}
  .abs{position:absolute}
  .photo{position:absolute;overflow:hidden}
  .heading{font-family:"Roboto Condensed",Arial,sans-serif;font-weight:700;color:var(--teal);text-transform:uppercase;line-height:1}

  /* front */
  .brand{left:20px;top:46px;display:flex;align-items:center;gap:8px}
  .brand__dot{width:14px;height:14px;border-radius:50%;background:var(--teal)}
  .brand__name{font-size:24px;font-weight:400;color:var(--teal);line-height:1}
  .brand__tag{left:42px;top:76px;font-size:7px;color:var(--ink);letter-spacing:.5px;text-transform:uppercase}
  .about-title{left:20px;top:150px;font-size:38px}
  .photo--feet{left:205px;top:30px;width:235px;height:245px;border-radius:125px 0 0 125px;background:linear-gradient(135deg,#6f8a4a,#c9a48c 55%,#5e7a3c);z-index:2}
  .about-band{left:0;top:225px;width:440px;height:195px;background:var(--teal)}
  .photo--artist{left:8px;top:225px;width:170px;height:190px;border-radius:0 95px 95px 0;background:linear-gradient(135deg,#7a5a40,#d8b49c 50%,#3aa9c4);z-index:3}
  .about-text{left:190px;top:282px;width:238px;font-size:8.6px;line-height:11px;color:var(--white);text-align:right;z-index:3}
  .services{left:0;top:420px;width:440px;height:190px;background:linear-gradient(180deg,var(--white),var(--soft))}
  .services-title{left:190px;top:430px;font-size:24px}
  .service{position:absolute;width:210px;display:flex;gap:6px;align-items:flex-start}
  .service__photo{flex:0 0 66px;height:66px;border-radius:50%}
  .service__body h3{font-size:7.5px;font-weight:700;color:var(--teal);text-transform:uppercase;margin-bottom:2px}
  .service__body p{font-size:6.2px;line-height:7.6px;color:var(--ink)}
  .service--kids{left:8px;top:462px}
  .service--belly{left:222px;top:462px}
  .service--wounds{left:8px;top:538px}
  .service--glitter{left:222px;top:538px}

  /* back */
  .offers{left:0;top:0;width:440px;height:300px;background:var(--teal);border-bottom-right-radius:170px}
  .offers-title{left:0;top:44px;width:440px;text-align:center;font-size:22px;color:var(--white)}
  .offer{position:absolute;width:180px;color:var(--white)}
  .offer h3{font-size:10px;font-weight:700;text-transform:uppercase;margin-bottom:3px}
  .offer p{font-size:9px;font-weight:300;line-height:11px}
  .offer--glitter{left:30px;top:100px}
  .offer--wounds{left:235px;top:100px}
  .offer--kids{left:30px;top:180px}
  .offer--belly{left:235px;top:180px}
  .works-title{left:200px;top:312px;font-size:22px}
  .gallery{left:0;top:345px;width:440px;height:180px;display:grid;grid-template-columns:repeat(3,1fr);grid-template-rows:repeat(2,1fr);gap:4px}
  .gallery .photo{position:relative}
  .contact-band{left:0;top:529px;width:440px;height:93px;background:var(--teal)}
  .contact-tab{left:0;top:510px;width:200px;height:112px;background:var(--teal-dark);border-top-right-radius:60px}
  .contact-title{left:26px;top:560px;font-size:24px;color:var(--white)}
  .contact-list{left:215px;top:545px;list-style:none;color:var(--white);font-size:10px;line-height:20px}
  .contact-list li{display:flex;align-items:center;gap:8px}
  .contact-list svg{width:12px;height:12px;fill:none;stroke:var(--white);stroke-width:2}
</style>
</head>
<body>

<section class="sheet sheet--back" aria-label="Flyer Rückseite">
  <div class="abs offers"></div>
  <h2 class="abs heading offers-title">Meine Leistungen</h2>
  <div class="offer offer--glitter"><h3>Meine Leistungen</h3><p>Glitzertattoos – Funkelnde Kunstwerke für den besonderen Glamour!</p></div>
  <div class="offer offer--wounds"><h3>Wunden Schminken</h3><p>Realistische Effekte, um Verletzungen und Grusel-Looks zum Leben zu erwecken!</p></div>
  <div class="offer offer--kids"><h3>Kinderschminken</h3><p>Kinderschminken – Kreative Verwandlung für kleine Abenteurer!</p></div>
  <div class="offer offer--belly"><h3>Belly Paint</h3><p>Schwangerschaftsbemalung – Kunstvolle Designs für Ihren wachsenden Bauch, einzigartig verwandelt!</p></div>

  <h2 class="abs heading works-title">Meine Arbeiten</h2>
  <div class="abs gallery">
    <div class="photo" role="img" aria-label="Foto: Glitzertattoo Löwe am Arm" style="background:linear-gradient(135deg,#c98a62,#6b4a36)"></div>
    <div class="photo" role="img" aria-label="Foto: Kind wird geschminkt" style="background:linear-gradient(135deg,#b36a5c,#3d3a3a)"></div>
    <div class="photo" role="img" aria-label="Foto: Glitzertattoo in Pink am Arm" style="background:linear-gradient(135deg,#d9a28c,#b04fa0)"></div>
    <div class="photo" role="img" aria-label="Foto: Blaues Glitzertattoo am Arm" style="background:linear-gradient(135deg,#c7a040,#3f7fc8)"></div>
    <div class="photo" role="img" aria-label="Foto: Schminken bei einer Veranstaltung" style="background:linear-gradient(135deg,#6b5240,#3aa9c4)"></div>
    <div class="photo" role="img" aria-label="Foto: Bemalter Babybauch" style="background:linear-gradient(135deg,#5a4232,#c8c8c8)"></div>
  </div>

  <div class="abs contact-band"></div>
  <div class="abs contact-tab"></div>
  <h2 class="abs heading contact-title">Kontakt</h2>
  <ul class="abs contact-list">
    <li><svg viewBox="0 0 24 24"><path d="M12 22s7-7 7-12a7 7 0 0 0-14 0c0 5 7 12 7 12z"/><circle cx="12" cy="10" r="2.5"/></svg>04567 Birkenau OT Talheim</li>
    <li><svg viewBox="0 0 24 24"><path d="M5 3h4l2 5-2.5 1.5a11 11 0 0 0 6 6L16 13l5 2v4a2 2 0 0 1-2 2A16 16 0 0 1 3 5a2 2 0 0 1 2-2z"/></svg>0160 / 12 34 567</li>
    <li><svg viewBox="0 0 24 24"><rect x="3" y="5" width="18" height="14" rx="1"/><path d="M3 6l9 7 9-7"/></svg>info@frau-sonnenfeld.de</li>
  </ul>
</section>

<section class="sheet sheet--front" aria-label="Flyer Vorderseite">
  <div class="abs brand"><span class="brand__dot"></span><span class="brand__name">Frau Sonnenfeld</span></div>
  <div class="abs brand__tag">Kinderschminken &amp; Glitzer Tattoos</div>
  <h1 class="abs heading about-title">Über mich</h1>
  <div class="photo photo--feet" role="img" aria-label="Foto: Glitzertattoos an Kinderbeinen auf einer Wiese"></div>

  <div class="abs about-band"></div>
  <div class="photo photo--artist" role="img" aria-label="Foto: Künstlerin bemalt eine Schulter"></div>
  <p class="abs about-text">Frau Sonnenfeld – Kreative Kinderschminken und glitzernde Tattoos für kleine Abenteurer:innen! Tauchen Sie ein in eine Welt voller Fantasie und Spaß, während wir die kleinen Gesichter mit wunderschönen Farben und magischem Glitzer zum Strahlen bringen. Entdecken Sie unser vielfältiges Angebot an bezaubernden Designs und verwandeln Sie sich in Ihr Lieblingswesen. Ob bunte Schmetterlinge, mutige Superhelden oder glitzernde Einhörner – wir machen jeden Moment zu einem unvergesslichen Erlebnis. Lassen Sie die Kinderaugen leuchten und erleben Sie magische Momente mit Frau Sonnenfeld.</p>

  <div class="abs services"></div>
  <h2 class="abs heading services-title">Leistungen</h2>
  <div class="service service--kids">
    <div class="service__photo" role="img" aria-label="Foto: Kinderschminken auf einem Fest" style="background:linear-gradient(135deg,#8a6a50,#d04f8a)"></div>
    <div class="service__body"><h3>Kinderschminken</h3><p>Verzaubern Sie die kleinen Gäste auf Ihrem Event mit unserem Kinderschminken! Lassen Sie Ihre Gesichter in leuchtenden Farben erstrahlen und schaffen Sie unvergessliche Erinnerungen für alle. Buchen Sie jetzt und bringen Sie magischen Spaß auf Ihre Veranstaltung!</p></div>
  </div>
  <div class="service service--belly">
    <div class="service__body"><h3>Belly Paint</h3><p>Entdecken Sie die zauberhafte Welt der Belly Paints! Verwandeln Sie Ihren Babybauch in eine Leinwand für kreative und bezaubernde Kunstwerke. Wir zaubern ein einzigartiges Design, das Ihre Schwangerschaft auf wundervolle Weise feiert. Buchen Sie jetzt Ihre Session!</p></div>
    <div class="service__photo" role="img" aria-label="Foto: Bemalter Babybauch" style="background:linear-gradient(135deg,#5a4232,#c8c8c8)"></div>
  </div>
  <div class="service service--wounds">
    <div class="service__photo" role="img" aria-label="Foto: Wundenschminken im Gesicht" style="background:linear-gradient(135deg,#e0b8a0,#8a1a2a)"></div>
    <div class="service__body"><h3>Wunden Schminken</h3><p>Erwecken Sie fesselnde Geschichten zum Leben und verblüffen Sie Ihre Freunde mit professionellem Wunden-Schminken! Tauchen Sie ein in die Welt der Special Effects und lassen Sie Ihre Fantasie Wirklichkeit werden. Buchen Sie jetzt Ihre Session!</p></div>
  </div>
  <div class="service service--glitter">
    <div class="service__body"><h3>Glitzer Tattoos</h3><p>Entdecken Sie die Magie der Glitzer-Tattoos, die wasserfest sind und je nach Pflege bis zu 2 Wochen lang halten! Wenn Sie eine Veranstaltung planen, insbesondere bei heißen Temperaturen, empfehlen wir Ihnen diese fantastischen Tattoos.</p></div>
    <div class="service__photo" role="img" aria-label="Foto: Glitzertattoo am Arm" style="background:linear-gradient(135deg,#d9a28c,#9a4fb0)"></div>
  </div>
</section>

</body>
</html>
```